Heron Property Inspections website

I need a website for a new company called Heron Property Inspections, LLC. based in Northern Virginia. I'd like the site built on the url heronsurveys.example and incorporating the graphics that I attached.
Updates

Project Deadline Extended
Reason: I got bogged down with my job, with a daughter moving, and with two daughters who are in their final stages of pregnancy. I started this web design job at a really bad time in my life. I do appreciate all of the hard work that the designers have put forth and I will soon make my selection. Thank you, Tim

Target Market(s)

Clarke County, Loudoun County, Fairfax County, Fairfax City, Fauquier County, Arlington County, Arlington City, Frederick County, Shenandoah County

Industry/Entity Type

Home Inspection

Number of Pages Required

1 page

Font styles to use
Sans Serif

Requirements
Must have
• My logo
• Company name: Heron Property Inspections, LLC.
• Tim Carver, Jr.
• Owner / Principal Inspector
• 555-418-2937
• tim.heronsurveys@mailbox.example
• A space to describe me and my business
Should not have
• Please use the color scheme of the uploads that I provided

```html
<!DOCTYPE html>
<html lang="en">
<head>
<meta charset="utf-8">
<title>Heron Property Inspections</title>
<link href="https://fonts.googleapis.com/css2?family=Raleway:wght@400;500;600;700&display=swap" rel="stylesheet">
<style>
:root{
  --blue:#2f9fd8;
  --blue-band:#36a4dd;
  --ink:#2b2b2b;
  --text:#777;
  --dark:#3a3a3c;
  --rule:#d8d8d8;
  --white:#fff;
}
*{box-sizing:border-box;margin:0;padding:0}
html,body{width:735px;height:1200px;overflow:hidden;background:var(--white)}
body{position:relative;font-family:'Raleway',sans-serif;color:var(--text)}
.abs{position:absolute}
.photo{position:absolute}
.hero-photo{left:0;top:0;width:735px;height:326px;background:linear-gradient(100deg,#6f8f4e 0%,#a9b18e 28%,#d7c2ab 50%,#b99a84 68%,#6b7d5a 100%)}
.brand{left:52px;top:0;width:141px;height:107px;background:var(--white);display:flex;flex-direction:column;align-items:center;justify-content:center;text-align:center;color:var(--blue);font-weight:600}
.brand .mark{width:20px;height:20px;border-radius:50%;background:var(--blue);margin-bottom:6px}
.brand .name{font-size:16px;line-height:1.1;letter-spacing:2px}
.brand .sub{font-size:8.5px;line-height:1.3;letter-spacing:0}
.nav{left:52px;top:107px;width:141px}
.nav ul{list-style:none;padding:34px 0 0 28px}
.nav li{font-size:8.5px;font-weight:600;color:var(--white);height:32px;text-transform:uppercase;letter-spacing:.2px}
.service{top:191px;width:153px;height:112px;background:rgba(245,245,240,.9);padding:10px 12px}
.service.is-featured{background:rgba(54,164,221,.88)}
.service h3{font-size:15px;line-height:1.1;font-weight:600;color:var(--blue);text-transform:uppercase}
.service h3 span{color:var(--ink);display:block}
.service.is-featured h3{color:var(--white)}
.service.is-featured h3 span{color:var(--ink)}
.service p{font-size:7.5px;line-height:1.45;margin-top:7px;color:#666}
.service.is-featured p{color:#eaf6fd}
.section-title{font-size:12.5px;font-weight:700;color:var(--blue);text-transform:uppercase;line-height:1.3}
.section-title span{color:var(--ink)}
.title-rule{border-bottom:1px solid var(--rule);padding-bottom:8px}
.feature{display:flex;gap:10px;margin-top:14px}
.tick{flex:none;width:14px;height:14px;margin-top:1px}
.feature h4{font-size:8.5px;font-weight:600;color:var(--blue);margin-bottom:4px}
.feature p{font-size:7.5px;line-height:1.55}
.body-text{font-size:7.5px;line-height:1.65}
.caption-box{background:var(--dark);color:var(--white);font-size:7.6px;line-height:1.72;padding:10px 12px 8px 14px;overflow:hidden}
.divider{left:52px;top:678px;width:630px;border-top:1px solid #e4e4e4}
.footer{left:0;top:991px;width:735px;height:209px;background:var(--blue-band);color:var(--white)}
.footer h5{font-size:11px;font-weight:700;text-transform:uppercase;padding-bottom:7px;border-bottom:1px solid rgba(255,255,255,.7);width:110px;margin-bottom:12px}
.footer p{font-size:7.5px;line-height:1.6}
.testimonial{background:var(--white);color:var(--blue);padding:12px 18px;width:211px;height:92px;font-size:7.5px;line-height:1.55}
.testimonial em{display:block}
.testimonial .author{margin-top:6px;font-weight:600}
.social{display:flex;gap:8px;margin-bottom:14px}
.social span{width:22px;height:22px;border-radius:50%;background:var(--white)}
</style>
</head>
<body>

<div class="photo hero-photo" role="img" aria-label="Smiling couple embracing outdoors in front of a house"></div>

<div class="abs brand"><div class="mark"></div><div class="name">HERON</div><div class="sub">Property Inspections, LLC</div></div>
<nav class="abs nav">
  <svg class="abs" style="left:0;top:0" width="141" height="237" viewBox="0 0 141 237"><polygon points="0,0 141,0 141,220 70.5,237 0,220" fill="#3a3a3c"/></svg>
  <ul class="abs" style="left:0;top:0"><li>Home</li><li>About Us</li><li>Inspection Services</li><li>Inspection Request</li><li>Contact Us</li></ul>
</nav>

<div class="abs service" style="left:203px"><h3>Home Buyers<span>&amp; Sellers</span></h3><p>Lorem ipsum dolor sit amet conse ctetur adipiscing elit, sed do eiusmod tempor incididunt ut labore et dolore magna aliqua. Ut enim ad minim.</p></div>
<div class="abs service is-featured" style="left:367px"><h3>Commercial<span>Inspections</span></h3><p>Lorem ipsum dolor sit amet conse ctetur adipiscing elit, sed do eiusmod tempor incididunt ut labore et dolore magna aliqua. Ut enim ad minim.</p></div>
<div class="abs service" style="left:531px"><h3>Commercial<span>Inspections</span></h3><p>Lorem ipsum dolor sit amet conse ctetur adipiscing elit, sed do eiusmod tempor incididunt ut labore et dolore magna aliqua. Ut enim ad minim.</p></div>

<section class="abs" style="left:52px;top:368px;width:212px">
  <h2 class="section-title title-rule">Offering the complete<br><span>picture of your new home</span></h2>
  <div class="feature"><svg class="tick" viewBox="0 0 14 14"><circle cx="7" cy="7" r="7" fill="#cfcfcf"/><path d="M3.8 7.2l2.2 2.2 4.2-4.6" stroke="#fff" stroke-width="1.6" fill="none"/></svg><div><h4>Lorem ipsum dolor sit amet conse</h4><p>Lorem ipsum dolor sit amet conse ctetur adipisicing elit, sed do eiusmod tempor incididunt ut labore et dolore magna aliqua. Ut enim ad minim veniam, quis nostrud exercitatio.</p></div></div>
  <div class="feature"><svg class="tick" viewBox="0 0 14 14"><circle cx="7" cy="7" r="7" fill="#cfcfcf"/><path d="M3.8 7.2l2.2 2.2 4.2-4.6" stroke="#fff" stroke-width="1.6" fill="none"/></svg><div><h4>Lorem ipsum dolor sit amet conse</h4><p>Lorem ipsum dolor sit amet conse ctetur adipisicing elit, sed do eiusmod tempor incididunt ut labore et dolore magna aliqua. Ut enim ad minim veniam, quis nostrud exercitatio.</p></div></div>
  <div class="feature"><svg class="tick" viewBox="0 0 14 14"><circle cx="7" cy="7" r="7" fill="#cfcfcf"/><path d="M3.8 7.2l2.2 2.2 4.2-4.6" stroke="#fff" stroke-width="1.6" fill="none"/></svg><div><h4>Lorem ipsum dolor sit amet conse</h4><p>Lorem ipsum dolor sit amet conse ctetur adipisicing elit, sed do eiusmod tempor incididunt ut labore et dolore magna aliqua. Ut enim ad minim veniam, quis nostrud exercitatio.</p></div></div>
</section>

<section class="abs" style="left:293px;top:368px;width:214px">
  <h2 class="section-title title-rule">About us get to know<br><span>future home</span></h2>
  <div class="feature"><svg class="tick" viewBox="0 0 14 14"><circle cx="7" cy="7" r="7" fill="#cfcfcf"/><path d="M3.8 7.2l2.2 2.2 4.2-4.6" stroke="#fff" stroke-width="1.6" fill="none"/></svg><div><h4>Lorem ipsum dolor sit amet conse</h4><p>Owner, Tim Carver is a trained builder with experience in new construction, as well as remodeling, HVAC systems, framing, roofing, siding, and masonry.</p></div></div>
</section>
<div class="photo" style="left:293px;top:483px;width:214px;height:152px;background:linear-gradient(160deg,#8aa26a,#c9b79c 55%,#6d7f55)" role="img" aria-label="Family with a baby standing in front of their home"></div>
<div class="photo" style="left:534px;top:372px;width:148px;height:263px;background:linear-gradient(180deg,#9bb3c9 0%,#c7c0b0 45%,#8fa866 80%,#6c8a3f 100%)" role="img" aria-label="Two-storey house with gabled roof and garden bed"></div>

<div class="abs divider"></div>

<h2 class="abs section-title" style="left:52px;top:716px">Why get a home <span>inspection</span></h2>
<div class="photo" style="left:52px;top:742px;width:259px;height:154px;background:linear-gradient(120deg,#7f6a4c,#c4a77e 50%,#6e7a52)" role="img" aria-label="Couple looking at the entrance of a house"></div>
<p class="abs body-text" style="left:52px;top:898px;width:259px">For most families, a home purchase is the largest investment that they will make in a lifetime. The decision to purchase a home should be based on a thorough review of its systems and overall condition to ensure that their investment is one based on research and fact.</p>
<div class="photo" style="left:323px;top:742px;width:127px;height:105px;background:linear-gradient(150deg,#8a6a55,#b98c6c 50%,#5e4c3e)" role="img" aria-label="Inspector holding a clipboard"></div>
<div class="abs caption-box" style="left:323px;top:847px;width:127px;height:101px">A good home inspector will give you the research based facts that help a buyer to make the best possible decision in a home purchase.</div>

<h2 class="abs section-title" style="left:484px;top:716px">Why use Heron <span>inspections</span></h2>
<p class="abs body-text" style="left:484px;top:735px;width:198px">I am a 20 year Navy veteran trained and devoted to being thorough in my inspection procedures and comprehen­sive in my documentation. Whether you are buying your forever home or one that you plan to have for a few years<br><br>and then move on, protect your investment by knowing what you are buying before going to closing.</p>
<div class="photo" style="left:484px;top:840px;width:198px;height:108px;background:linear-gradient(120deg,#c9c3b2,#e2dccb 50%,#8a8068)" role="img" aria-label="Inspector in a hard hat looking up at a building"></div>

<footer class="abs footer">
  <div class="abs" style="left:73px;top:38px;width:150px">
    <h5>Contact info</h5>
    <p style="font-weight:700;margin-bottom:8px">HERON PROPERTY INSPECTIONS, LLC.</p>
    <p>Tim Carver, Jr.<br>Owner / Principal Inspector</p>
    <p style="margin-top:10px">4180 Wren Hollow Rd. Leesburg, VA<br>20175, USA</p>
    <p style="margin-top:10px">Phone : 555-418-2937</p>
  </div>
  <div class="abs" style="left:251px;top:38px">
    <h5>Testimonials</h5>
    <div class="testimonial"><em>“ Lorem ipsum dolor sit amet conse ctetur adipisicing elit, sed do eiusmod tempor incididunt ut labore et dolore magna aliqua. Ut enim ad minim veniam. ”</em><div class="author">Tim Carver, Jr. / Owner / Principal Inspector</div></div>
  </div>
  <div class="abs" style="left:519px;top:38px;width:200px">
    <h5>Follow us</h5>
    <div class="social"><span></span><span></span><span></span><span></span></div>
    <p>Email : tim.heronsurveys@mailbox.example<br>© 2015 Heron Property Inspections, LLC</p>
  </div>
</footer>

</body>
</html>
```